Marlowe Hollis College Sales Presentation to demonstrate instructional design process

We would like the Powerpoint to be re-designed. The content on the screen and in the notes sections must remain the same but it can all be re-styled to look more modern and professional. Please use our logo colors and the final design should communicate professionalism and experience. We typically use the blue and white colors predominately and use the red in the logo sparingly for emphasis.

Target Market(s)

Audience of college educators, sales people, instructional designers, and leaders

Industry/Entity Type

Higher Education and Professional Services

Font styles to use
Sans Serif

Colors
0054AA
0677BA
7BADD7
CADEEF
E8F1F8
EB3D1F
EC4F4E
F09395
F8D3D4
FCEDEE

Requirements
Must have
• clear visuals, same verbiage we have supplied, colorful and artful design
Nice to have
• some animations between slides would be nice.
Should not have
• It should not use red text on black backgrounds.

```html
<!DOCTYPE html>
<html lang="en">
<head>
<meta charset="utf-8">
<title>Marlowe Hollis College — Instructional Design Proposal Deck</title>
<link href="https://fonts.googleapis.com/css2?family=Figtree:wght@400;500;600;700&display=swap" rel="stylesheet">
<style>
:root{
  --blue:#0054AA; --blue-mid:#0677BA; --blue-soft:#7BADD7; --blue-pale:#CADEEF; --blue-mist:#E8F1F8;
  --red:#EB3D1F; --red-deep:#B3121A; --red-soft:#F09395;
  --navy:#0B2A66; --navy-deep:#050B1C;
  --ink:#1d1d24; --grey:#8a8f99; --page:#ebebeb; --white:#fff;
}
*{box-sizing:border-box;margin:0;padding:0}
html,body{width:717px;height:1200px;overflow:hidden;background:var(--page)}
body{font-family:"Figtree",sans-serif;color:var(--ink)}
.stage{width:1410px;height:2360px;transform:scale(.5085);transform-origin:0 0;position:relative}
.slide{position:absolute;width:594px;height:330px;background:var(--white);overflow:hidden;box-shadow:0 6px 14px rgba(0,0,0,.12)}
.slide.dark{background:linear-gradient(180deg,#0c3580 0%,#071a44 55%,var(--navy-deep) 100%);color:var(--white)}
.c1{left:95px}.c2{left:720px}
.r1{top:104px}.r2{top:469px}.r3{top:833px}.r4{top:1197px}.r5{top:1561px}.r6{top:1925px}
.abs{position:absolute}
.dash{position:absolute;left:17px;top:16px;width:20px;height:3px}
.dash::before{content:"";position:absolute;left:0;top:0;width:14px;height:3px;background:var(--blue);border-radius:2px}
.dash::after{content:"";position:absolute;left:16px;top:0;width:5px;height:3px;background:var(--red);border-radius:2px}
.dark .dash::before{background:var(--white)}
.title{position:absolute;left:17px;top:22px;font-size:18px;font-weight:500;letter-spacing:.1px}
.title .accent{color:var(--red)}
.brand{position:absolute;right:16px;top:20px;display:flex;align-items:center;gap:4px;font-size:14px;font-weight:700;color:var(--blue)}
.brand i{width:15px;height:15px;border-radius:50%;background:var(--blue);display:block}
.dark .brand{color:var(--white)}
.dark .brand i{background:var(--white)}
.url{position:absolute;left:17px;bottom:16px;font-size:7.5px;color:var(--grey)}
.dark .url{color:var(--white)}
.pageno{position:absolute;right:17px;bottom:12px;font-size:7.5px;display:flex;align-items:center;gap:6px;font-weight:600}
.pageno b{display:block;width:1px;height:16px;background:var(--blue)}
.dark .pageno b{background:var(--white)}
.pageno span:last-child{font-weight:400;color:var(--blue)}
.dark .pageno span:last-child{color:var(--white)}
.card{position:absolute;background:var(--white);box-shadow:0 3px 10px rgba(0,0,0,.12)}
.tiny{font-size:6.5px;line-height:1.45;color:var(--grey)}
.small{font-size:7.5px;line-height:1.4}
.ph{position:absolute}
.ico{position:absolute;width:14px;height:14px}
.cover-brand{position:absolute;left:0;right:0;top:52px;display:flex;justify-content:center;align-items:center;gap:6px;font-size:17px;font-weight:700;color:var(--blue)}
.cover-brand i{width:30px;height:30px;border-radius:50%;background:var(--blue);display:block}
.cover-dash{position:absolute;left:275px;top:122px;width:44px;height:3px}
.cover-dash::before{content:"";position:absolute;left:0;width:30px;height:3px;background:var(--blue);border-radius:2px}
.cover-dash::after{content:"";position:absolute;left:34px;width:10px;height:3px;background:var(--red);border-radius:2px}
.cover-title{position:absolute;left:0;right:0;top:136px;text-align:center;font-size:19px;line-height:1.22;font-weight:500}
.cover-sub{position:absolute;left:0;right:0;top:195px;text-align:center;font-size:10.5px;line-height:1.6}
.member{position:absolute;top:105px;width:110px;text-align:center}
.member .face{width:68px;height:68px;border-radius:50%;margin:0 auto;border:3px solid var(--white);box-shadow:0 3px 8px rgba(0,0,0,.2)}
.member p{font-size:6.5px;line-height:1.9;margin-top:10px;color:#333}
.member small{display:block;font-size:6px;line-height:1.9;color:#555}
.tbl-head{position:absolute;left:35px;width:524px;top:120px;height:25px;background:#0d47a8;display:flex;align-items:center;font-size:8px;font-weight:500}
.tbl-head div,.tbl-row div{flex:1;text-align:center}
.tbl-row{position:absolute;left:35px;width:524px;top:152px;height:48px;background:rgba(30,45,80,.75);display:flex;align-items:center;font-size:6px;line-height:1.45;border-left:2px solid var(--blue-mid)}
.tbl-row div{border-right:1px solid rgba(255,255,255,.25);padding:0 3px}
.tbl-row div:last-child{border-right:0}
.btn{position:absolute;top:192px;width:72px;height:46px;display:flex;align-items:center;justify-content:center;font-size:7px;color:var(--grey);background:var(--white);box-shadow:0 3px 9px rgba(0,0,0,.12)}
.btn.on{background:var(--blue);color:var(--white)}
.deliv{position:absolute;width:150px;text-align:center;font-size:7px;line-height:1.6;color:#444}
.deliv .ico{position:relative;display:block;margin:0 auto 6px}
.ring-label{position:absolute;width:110px;text-align:center;font-size:6.5px;line-height:1.45}
.brand-card-name{position:absolute;left:0;right:0;top:78px;text-align:center;font-size:30px;font-weight:700;color:var(--blue)}
</style>
</head>
<body>
<main class="stage">

<section class="slide c1 r1" style="background:linear-gradient(135deg,#fff 60%,#f4f6fa 100%)">
  <div class="cover-brand"><i></i>Loomline</div>
  <div class="cover-dash"></div>
  <h1 class="cover-title">State of Westbrook Public Institutions of<br>Higher Education Request for Proposal</h1>
  <p class="cover-sub">Furnish and Deliver Instructional Design<br>and Media Production<br>1JNM2303</p>
  <p class="abs" style="left:20px;bottom:20px;font-size:7.5px;color:var(--blue)">January 2023</p>
  <p class="abs" style="right:22px;bottom:22px;font-size:7.5px;color:var(--blue)">www.loomline.com</p>
</section>

<section class="slide c2 r1" style="background:linear-gradient(135deg,#fff 30%,#eef0f4 55%,#fff 70%,#f1f3f6 100%)">
  <div class="dash"></div><h2 class="title">Meet the Team</h2>
  <div class="brand"><i></i>Loomline</div>
  <div class="member" style="left:25px"><div class="face" role="img" aria-label="Portrait of Daniel Reyes" style="background:linear-gradient(#c9ccd2,#5b6170)"></div><p>Daniel Reyes, PhD<small>COO</small></p></div>
  <div class="member" style="left:134px"><div class="face" role="img" aria-label="Portrait of Ruth Ellison" style="background:linear-gradient(#d98a6c,#a4402e)"></div><p>Ruth Ellison, MA<small>Research &amp;<br>Development Project<br>Director</small></p></div>
  <div class="member" style="left:242px"><div class="face" role="img" aria-label="Portrait of Carla Vance" style="background:linear-gradient(#e5d9cf,#4a3a30)"></div><p>Carla Vance, MA<small>CEO</small></p></div>
  <div class="member" style="left:349px"><div class="face" role="img" aria-label="Portrait of Ingrid Holloway" style="background:linear-gradient(#e9c0a4,#b5553d)"></div><p>Ingrid Holloway, MA<small>Senior Manager of<br>Instructional Design</small></p></div>
  <div class="member" style="left:458px"><div class="face" role="img" aria-label="Portrait of Tessa Marlin" style="background:linear-gradient(#d8c6b8,#2a2326)"></div><p>Tessa Marlin, CPACC<small>Vice President</small></p></div>
  <p class="url">www.loomline.com</p><div class="pageno"><span>page</span><b></b><span>2</span></div>
</section>

<section class="slide c1 r2">
  <div class="dash"></div><h2 class="title">Presentation Section</h2>
  <div class="brand"><i></i>Loomline</div>
  <div class="card" style="left:50px;top:78px;width:116px;height:84px;padding:26px 0 0 12px">
    <svg class="ico" style="right:10px;top:6px" viewBox="0 0 14 14"><circle cx="7" cy="5" r="3" fill="var(--blue)"/><path d="M2 14c0-4 2-5 5-5s5 1 5 5z" fill="var(--red)"/></svg>
    <p class="small">Woman / Minority Business</p><p class="tiny">Certified State of Westbrook<br>WMBE Woman/Minority<br>Business Enterprise</p></div>
  <div class="card" style="left:183px;top:78px;width:112px;height:84px;padding:26px 0 0 8px">
    <svg class="ico" style="right:10px;top:6px" viewBox="0 0 14 14"><path d="M3 0h3l2 5M11 0H8L6 5" stroke="var(--red)" stroke-width="2" fill="none"/><circle cx="7" cy="9" r="4.5" fill="var(--blue)"/></svg>
    <p class="small">17 Years of Experience</p><p class="tiny">In Business since 2006</p></div>
  <div class="card" style="left:50px;top:177px;width:116px;height:86px;padding:22px 0 0 12px">
    <svg class="ico" style="right:10px;top:6px" viewBox="0 0 14 14"><rect x="1" y="1" width="12" height="8" fill="none" stroke="var(--blue)" stroke-width="1.4"/><path d="M3 7l3-3 2 2 3-3" stroke="var(--red)" stroke-width="1.2" fill="none"/><path d="M5 14l2-5 2 5" stroke="var(--blue)" fill="none"/></svg>
    <p class="small">Primary Focus</p><p class="tiny">We are dedicated to creating<br>top-notch educational<br>experiences through<br>collaboration with faculty and<br>subject matter experts.</p></div>
  <div class="card" style="left:183px;top:177px;width:112px;height:86px;padding:22px 0 0 8px">
    <svg class="ico" style="right:10px;top:6px" viewBox="0 0 14 14"><rect x="1" y="6" width="3" height="8" fill="var(--blue)"/><rect x="5.5" y="3" width="3" height="11" fill="var(--red)"/><rect x="10" y="5" width="3" height="9" fill="var(--blue)"/></svg>
    <p class="small">Principles</p><p class="tiny">Communication, attention, and<br>passion</p></div>
  <div class="card" style="left:348px;top:78px;width:189px;height:185px">
    <p class="brand-card-name">Loomline</p>
  </div>
  <p class="url">www.loomline.com</p><div class="pageno"><span>page</span><b></b><span>3</span></div>
</section>

<section class="slide c2 r2">
  <div class="dash"></div><h2 class="title">Process</h2>
  <p class="abs" style="left:17px;top:42px;font-size:6px;color:#555">Overview of Our Process</p>
  <div class="brand"><i></i>Loomline</div>
  <div class="ph" role="img" aria-label="Close-up photo of interlocking metal gears" style="left:37px;top:82px;width:248px;height:164px;background:radial-gradient(circle at 30% 50%,#e8ebf0,#6d7380 55%,#1e2430 100%)"></div>
  <p class="abs" style="left:311px;top:93px;width:250px;font-size:6.8px;line-height:1.95;color:#333">Lorem ipsum dolor sit amet, consectetuer adipiscing elit. Maecenas porttitor congue massa. Fusce posuere, magna sed pulvinar ultricies, purus lectus malesuada libero, sit amet commodo magna eros quis urna.Nunc viverra imperdiet enim. Fusce est. Vivamus a tellus. Pellentesque habitant morbi tristique senectus et netus et malesuada fames ac turpis egestas.</p>
  <div class="btn" style="left:310px">Process One</div>
  <div class="btn on" style="left:395px">Process Two</div>
  <div class="btn" style="left:481px">Process Three</div>
  <p class="url">www.loomline.com</p><div class="pageno"><span>page</span><b></b><span>4</span></div>
</section>

<section class="slide c1 r3">
  <div class="dash"></div><h2 class="title">Our Process Philosophy</h2>
  <div class="brand"><i></i>Loomline</div>
  <div class="ph" role="img" aria-label="Photo of smiling educators meeting at a laptop" style="left:0;top:102px;width:256px;height:141px;background:linear-gradient(90deg,#c8c4bb,#a59a8a 45%,#e1ddd5 75%,#8c8478)"></div>
  <div class="card" style="left:250px;top:135px;width:93px;height:78px;text-align:center;padding-top:12px">
    <svg class="ico" style="position:relative;display:block;margin:0 auto 10px" viewBox="0 0 14 14"><circle cx="7" cy="6" r="5" fill="var(--blue)"/><circle cx="7" cy="6" r="2" fill="var(--red)"/><rect x="5" y="11" width="4" height="3" fill="var(--blue)"/></svg>
    <p class="tiny" style="color:#555">Inspire Faculty</p></div>
  <div class="card" style="left:355px;top:135px;width:93px;height:78px;text-align:center;padding-top:12px">
    <svg class="ico" style="position:relative;display:block;margin:0 auto 10px" viewBox="0 0 14 14"><rect x="0" y="0" width="6.5" height="6.5" fill="var(--blue)"/><rect x="7.5" y="0" width="6.5" height="6.5" fill="var(--red)"/><rect x="0" y="7.5" width="6.5" height="6.5" fill="var(--red)"/><rect x="7.5" y="7.5" width="6.5" height="6.5" fill="var(--blue)"/></svg>
    <p class="tiny" style="color:#555">Deliver Powerful and<br>Effective Course<br>Designs</p></div>
  <div class="card" style="left:460px;top:135px;width:93px;height:78px;text-align:center;padding-top:12px">
    <svg class="ico" style="position:relative;display:block;margin:0 auto 10px" viewBox="0 0 14 14"><path d="M7 7L2 2M7 7l5-5M7 7L2 12M7 7l5 5" stroke="var(--blue)"/><circle cx="7" cy="7" r="2.5" fill="var(--red)"/><circle cx="2" cy="2" r="1.5" fill="var(--blue)"/><circle cx="12" cy="2" r="1.5" fill="var(--blue)"/><circle cx="2" cy="12" r="1.5" fill="var(--blue)"/><circle cx="12" cy="12" r="1.5" fill="var(--blue)"/></svg>
    <p class="tiny" style="color:#555">Equip Faculty with<br>Cutting-Edge Concepts,<br>Tools, Research, &amp; Best<br>Practices</p></div>
  <p class="url">www.loomline.com</p><div class="pageno"><span>page</span><b></b><span>5</span></div>
</section>

<section class="slide c2 r3">
  <div class="dash"></div><h2 class="title">Tangible Deliverables</h2>
  <div class="brand"><i></i>Loomline</div>
  <div class="card" style="left:220px;top:77px;width:152px;height:93px"></div>
  <div class="deliv" style="left:54px;top:92px"><svg class="ico" viewBox="0 0 14 14"><circle cx="4" cy="3" r="2" fill="var(--blue)"/><rect x="1" y="6" width="6" height="8" fill="var(--blue)"/><rect x="8" y="1" width="5" height="4" fill="var(--red)"/><rect x="8" y="7" width="5" height="7" fill="var(--blue)"/></svg>Instructionally sound and<br>accessible courses</div>
  <div class="deliv" style="left:222px;top:92px"><svg class="ico" viewBox="0 0 14 14"><rect x="1" y="2" width="12" height="2.5" fill="var(--red)"/><rect x="1" y="5.5" width="12" height="7" fill="none" stroke="var(--blue)" stroke-width="1.4"/><path d="M3 9h5" stroke="var(--blue)"/></svg>ID mapping<br>documents</div>
  <div class="deliv" style="left:389px;top:92px"><svg class="ico" viewBox="0 0 14 14"><circle cx="9" cy="9" r="4.5" fill="var(--blue)"/><circle cx="9" cy="9" r="1.8" fill="#fff"/><circle cx="3.5" cy="3.5" r="2.8" fill="var(--red)"/></svg>CB guided rubric</div>
  <div class="deliv" style="left:54px;top:222px"><svg class="ico" viewBox="0 0 14 14"><rect x="2" y="1" width="10" height="13" fill="none" stroke="var(--blue)" stroke-width="1.4"/><rect x="5" y="0" width="4" height="2.5" fill="var(--red)"/><path d="M4 6h6M4 9h6M4 11.5h4" stroke="var(--blue)"/></svg>Accessibility checklist</div>
  <div class="deliv" style="left:222px;top:222px"><svg class="ico" viewBox="0 0 14 14"><rect x="4" y="0" width="10" height="7" fill="var(--red)"/><circle cx="4" cy="7" r="2" fill="var(--blue)"/><rect x="1" y="9.5" width="6" height="4.5" fill="var(--blue)"/></svg>Workshops for Faculty</div>
  <div class="deliv" style="left:389px;top:222px"><svg class="ico" viewBox="0 0 14 14"><path d="M1 2l6 2v10L1 12z" fill="var(--blue)"/><path d="M13 2L7 4v10l6-2z" fill="var(--blue-mid)"/><path d="M7 4v10" stroke="var(--red)" stroke-width="1.2"/></svg>UI Faculty Hub</div>
  <p class="url">www.loomline.com</p><div class="pageno"><span>page</span><b></b><span>6</span></div>
</section>

<section class="slide dark c1 r4">
  <div class="dash"></div><h2 class="title">Communication Between MHC <span class="accent">Faculty and IDs</span></h2>
  <div class="brand"><i></i>Loomline</div>
  <div class="tbl-head"><div>Meetings</div><div>IDs</div><div>Profit Rate</div><div>Work-sheets</div><div>Shared Files</div><div>Work-shops</div><div style="flex:1.4">Faculty Hub</div></div>
  <div class="tbl-row"><div>Kickoff and<br>Weekly</div><div>Available via Video,<br>Email,&amp; Phone</div><div>Customized to<br>Client Needs</div><div>Document<br>Collaboration</div><div>Hosted on<br>DocSpace</div><div>Focused on Specific<br>Topics and Tools</div><div style="flex:1.4">Repository for Important<br>project Information and<br>Resources</div></div>
  <p class="url">www.loomline.com</p><div class="pageno"><span>page</span><b></b><span>7</span></div>
</section>

<section class="slide dark c2 r4">
  <div class="dash"></div><h2 class="title">Communication Between MHC <span class="accent">Staff and Loomline</span></h2>
  <div class="brand"><i></i>Loomline</div>
  <div class="tbl-head"><div style="flex:.8">Meetings</div><div>Report</div><div>Urgent Issues</div><div style="line-height:1.1">Multiple<br>Channels</div><div>Single POC</div><div>PM Web Portal</div><div style="flex:1.2">Faculty Hub</div></div>
  <div class="tbl-row"><div style="flex:.8">Kickoff and<br>Weekly</div><div>Provided Weekly</div><div>Available 24/7</div><div>Email, Phone, Video</div><div>Dedicated Single<br>Point of Contact</div><div>Real Time Project<br>Updates Available in<br>PM Portal</div><div style="flex:1.2">Repository for Important<br>project Information and<br>Resources</div></div>
  <p class="url">www.loomline.com</p><div class="pageno"><span>page</span><b></b><span>8</span></div>
</section>

<section class="slide c1 r5">
  <div class="dash"></div><h2 class="title">Risk Management</h2>
  <div class="brand"><i></i>Loomline</div>
  <svg class="ico" style="left:92px;top:90px" viewBox="0 0 14 14"><circle cx="6" cy="6" r="4.5" fill="none" stroke="var(--blue)" stroke-width="1.6"/><path d="M9.5 9.5L13 13" stroke="var(--blue)" stroke-width="2"/><circle cx="6" cy="6" r="1.8" fill="var(--red)"/></svg>
  <div class="abs" style="left:121px;top:84px"><p class="small">Avoid</p><p class="tiny">Lorem ipsum dolor sit amet,<br>joyo takan kame yaan ow.</p></div>
  <svg class="ico" style="left:92px;top:162px" viewBox="0 0 14 14"><path d="M1 6l4 4 8-8" stroke="var(--blue)" stroke-width="2.2" fill="none"/><path d="M1 10l3 3" stroke="var(--red)" stroke-width="2"/></svg>
  <div class="abs" style="left:121px;top:156px"><p class="small">Accept</p><p class="tiny">Lorem ipsum dolor sit amet,<br>joyo takan kame yaan ow.</p></div>
  <svg class="ico" style="left:92px;top:234px" viewBox="0 0 14 14"><rect x="1" y="5" width="3" height="9" fill="var(--blue)"/><rect x="5.5" y="8" width="3" height="6" fill="var(--blue)"/><rect x="10" y="10" width="3" height="4" fill="var(--red)"/></svg>
  <div class="abs" style="left:121px;top:228px"><p class="small">Mitigate</p><p class="tiny">Lorem ipsum dolor sit amet,<br>joyo takan kame yaan ow.</p></div>
  <svg class="abs" style="left:310px;top:76px" width="192" height="192" viewBox="-96 -96 192 192">
    <path d="M0,-64.5 A64.5 64.5 0 0 1 60.6,22.1" fill="none" stroke="#0a5bc0" stroke-width="63"/>
    <path d="M60.6,22.1 A64.5 64.5 0 0 1 -62.3,16.7" fill="none" stroke="#b50d12" stroke-width="63"/>
    <path d="M-62.3,16.7 A64.5 64.5 0 0 1 0,-64.5" fill="none" stroke="#0a3fa6" stroke-width="63"/>
    <text x="-62" y="-24" fill="#fff" font-size="11" font-family="Figtree,sans-serif">Avoid</text>
    <text x="42" y="-14" fill="#fff" font-size="11" font-family="Figtree,sans-serif">Mitigate</text>
    <text x="-25" y="73" fill="#fff" font-size="11" font-family="Figtree,sans-serif">Accept</text>
  </svg>
  <p class="url">www.loomline.com</p><div class="pageno"><span>page</span><b></b><span>9</span></div>
</section>

<section class="slide c2 r5">
  <div class="dash"></div><h2 class="title">Quality Standards</h2>
  <div class="brand"><i></i>Loomline</div>
  <div class="ph" role="img" aria-label="Faded photo of reviewers at a table behind a program badge" style="left:0;top:62px;width:594px;height:98px;background:linear-gradient(180deg,#f7f7f7,#e7e8ea 60%,#fafafa)"></div>
  <div class="abs" style="left:247px;top:72px;width:100px;height:68px;background:var(--red-deep);border-radius:4px;opacity:.85"></div>
  <div class="card" style="left:40px;top:160px;width:122px;height:102px;padding:12px 10px">
    <svg class="ico" style="left:10px;top:12px" viewBox="0 0 14 14"><circle cx="7" cy="6" r="5" fill="var(--blue)"/><circle cx="7" cy="6" r="2" fill="#fff"/><path d="M4 10l-1 4 4-2 4 2-1-4" fill="var(--red)"/></svg>
    <p class="tiny" style="padding-left:18px;color:#333;font-size:7px">Course Benchmark<br>Certified Team</p>
    <p class="tiny" style="margin-top:8px;font-size:6px">Course Benchmark certified and<br>Certified Professionals in<br>Accessibility Core<br>Competencies (CPACC)</p></div>
  <div class="card" style="left:170px;top:160px;width:123px;height:102px;padding:12px 10px">
    <svg class="ico" style="left:10px;top:12px" viewBox="0 0 14 14"><circle cx="7" cy="3" r="2.5" fill="var(--red)"/><circle cx="3" cy="7" r="2" fill="var(--blue)"/><circle cx="11" cy="7" r="2" fill="var(--blue)"/><rect x="0" y="10" width="14" height="4" fill="var(--blue)"/></svg>
    <p class="tiny" style="padding-left:18px;color:#333;font-size:7px">8 CB Higher Education<br>General Standards</p>
    <p class="tiny" style="margin-top:8px;font-size:6px">All courses are reviewed based<br>on the 8 CB Higher Education<br>General Standards</p></div>
  <div class="card" style="left:302px;top:160px;width:122px;height:102px;padding:12px 10px">
    <svg class="ico" style="left:10px;top:12px" viewBox="0 0 14 14"><circle cx="5" cy="3.5" r="3" fill="var(--blue)"/><path d="M0 13c0-4 2-6 5-6s5 2 5 6z" fill="var(--blue)"/><circle cx="11" cy="11" r="3" fill="var(--red)"/></svg>
    <p class="tiny" style="padding-left:18px;color:#333;font-size:7px">Copyright</p>
    <p class="tiny" style="margin-top:14px;font-size:6px">Special attention is paid to<br>ownership, citation<br>requirements, and copyright<br>usage</p></div>
  <div class="card" style="left:434px;top:160px;width:123px;height:102px;padding:12px 10px">
    <svg class="ico" style="left:10px;top:12px" viewBox="0 0 14 14"><rect x="2" y="1" width="10" height="13" fill="none" stroke="var(--blue)" stroke-width="1.4"/><rect x="5" y="0" width="4" height="2.5" fill="var(--red)"/><circle cx="7" cy="7" r="1.5" fill="var(--blue)"/><path d="M4 12c0-2 1.5-3 3-3s3 1 3 3" fill="var(--blue)"/></svg>
    <p class="tiny" style="padding-left:18px;color:#333;font-size:7px">WCAG And Section<br>508 Accessibility</p>
    <p class="tiny" style="margin-top:8px;font-size:6px">Dedicated to ensuring<br>equitable digital access for</p></div>
  <p class="url">www.loomline.com</p><div class="pageno"><span>page</span><b></b><span>10</span></div>
</section>

<section class="slide c1 r6">
  <div class="dash"></div><h2 class="title">Content Review and Revisions</h2>
  <div class="brand"><i></i>Loomline</div>
  <svg class="abs" style="left:0;top:110px" width="594" height="130" viewBox="0 0 594 130">
    <g fill="none" stroke-width="11">
      <circle cx="83" cy="62" r="42" stroke="#eef0f3"/>
      <path d="M41,62 A42 42 0 0 0 125,62" stroke="#0a4fb3"/>
      <circle cx="170" cy="62" r="42" stroke="#eef0f3"/>
      <path d="M128,62 A42 42 0 0 1 212,62" stroke="#0a3e9e"/>
      <circle cx="255" cy="62" r="42" stroke="#eef0f3"/>
      <path d="M213,62 A42 42 0 0 0 297,62" stroke="#0c2b6e"/>
      <circle cx="341" cy="62" r="42" stroke="#eef0f3"/>
      <path d="M299,62 A42 42 0 0 1 383,62" stroke="#6e0f18"/>
      <circle cx="427" cy="62" r="42" stroke="#eef0f3"/>
      <path d="M385,62 A42 42 0 0 0 469,62" stroke="#8a121a"/>
      <circle cx="512" cy="62" r="42" stroke="#eef0f3"/>
      <path d="M470,62 A42 42 0 0 1 554,62" stroke="#c0141b"/>
    </g>
    <g>
      <rect x="75" y="52" width="16" height="20" fill="none" stroke="var(--blue)" stroke-width="2"/><rect x="80" y="49" width="6" height="5" fill="var(--red)"/>
      <circle cx="168" cy="60" r="8" fill="none" stroke="var(--blue)" stroke-width="2.4"/><path d="M174 66l6 6" stroke="var(--blue)" stroke-width="3"/><circle cx="168" cy="60" r="3" fill="var(--red)"/>
      <circle cx="255" cy="55" r="6" fill="var(--red)"/><circle cx="247" cy="63" r="4" fill="var(--blue)"/><circle cx="263" cy="63" r="4" fill="var(--blue)"/><rect x="242" y="68" width="26" height="5" fill="var(--blue)"/>
      <circle cx="338" cy="54" r="5" fill="var(--blue)"/><path d="M330 74c0-8 3-12 8-12s8 4 8 12z" fill="var(--blue)"/><circle cx="348" cy="70" r="5" fill="var(--red)"/>
      <circle cx="427" cy="62" r="11" fill="none" stroke="var(--blue)" stroke-width="2.4"/><path d="M416 62h22M427 51c-5 6-5 16 0 22M427 51c5 6 5 16 0 22" stroke="var(--blue)" stroke-width="1.5" fill="none"/>
      <circle cx="512" cy="58" r="9" fill="var(--blue)"/><circle cx="512" cy="58" r="3.5" fill="#fff"/><path d="M506 66l-3 9 9-4 9 4-3-9" fill="var(--red)"/>
    </g>
  </svg>
  <p class="ring-label" style="left:115px;top:95px">SME/ID make<br>content changes</p>
  <p class="ring-label" style="left:286px;top:85px">Review for educational<br>effectiveness, accuracy, and<br>adherence to guidelines</p>
  <p class="ring-label" style="left:457px;top:104px">Course finalized</p>
  <p class="ring-label" style="left:28px;top:230px">ID identifies and<br>reviews content</p>
  <p class="ring-label" style="left:200px;top:230px">Content loaded into<br>LMS</p>
  <p class="ring-label" style="left:372px;top:230px">Course Benchmark and<br>Accessibility rubric reviews</p>
  <p class="url">www.loomline.com</p><div class="pageno"><span>page</span><b></b><span>11</span></div>
</section>

<section class="slide dark c2 r6" style="background:linear-gradient(180deg,#0c3580 0%,#081d4c 60%,#071637 100%)">
  <h2 class="abs" style="left:0;right:0;top:104px;text-align:center;font-size:34px;font-weight:500">Thank You</h2>
  <div class="abs" style="left:187px;top:153px;width:220px;height:1px;background:linear-gradient(90deg,transparent,var(--blue-soft),transparent)"></div>
  <p class="abs" style="left:140px;width:314px;top:168px;text-align:center;font-size:7px;line-height:1.85">Lorem ipsum dolor sit amet, consectetuer adipiscing elit. Maecen portion congue massa. Fusce posuere, magna sed pulvinar ultricies, purus lectus.</p>
  <div class="abs" style="left:240px;top:220px;width:18px;height:18px;border:1px solid #fff;border-radius:50%"></div>
  <div class="abs" style="left:288px;top:220px;width:18px;height:18px;border:1px solid #fff;border-radius:50%"></div>
  <div class="abs" style="left:336px;top:220px;width:18px;height:18px;border:1px solid #fff;border-radius:50%"></div>
</section>

</main>
</body>
</html>
```